Futuristic but clean CD Cover Design

I need a CD Cover design for my next EP. The music is electronic pop. I am looking for something clean but futuristic with neon colors .Name of band: peopleASponiesName of Album: CeylonI have attached my logo.I have also attached CD covers of the color scheme and clean look I am looking for.Thanks

Industry/Entity Type

Film Production

Requirements
Must have
• A clean future look. The music is electronic pop.

```html
<!DOCTYPE html>
<html lang="en">
<head>
<meta charset="utf-8">
<title>Mirvane — kettlesINorbit</title>
<link rel="stylesheet" href="https://fonts.googleapis.com/css2?family=Josefin+Sans:wght@400;600&display=swap">
<style>
  :root {
    --teal-bright: #5fe3ec;
    --teal-mid: #2f9fb0;
    --teal-deep: #1d4f5e;
    --maroon: #5a1a24;
    --violet: #4a3f8f;
    --ink: #241a26;
    --title-white: #ffffff;
    --band-gold: #d8c24a;
  }
  html, body {
    margin: 0;
    padding: 0;
    width: 1200px;
    height: 1200px;
    overflow: hidden;
    background: var(--ink);
  }
  .cover {
    position: relative;
    width: 1200px;
    height: 1200px;
    overflow: hidden;
  }
  .cover-art {
    position: absolute;
    inset: 0;
    display: block;
  }
  .title-row {
    position: absolute;
    top: 116px;
    left: 160px;
    display: flex;
    align-items: center;
    font-family: "Josefin Sans", sans-serif;
    font-size: 46px;
    line-height: 1;
  }
  .album-title {
    color: var(--title-white);
    font-weight: 400;
    letter-spacing: 0.98em;
    text-transform: uppercase;
  }
  .title-divider {
    display: inline-block;
    width: 4px;
    height: 34px;
    background: var(--title-white);
    margin: 0 38px 0 -4px;
  }
  .band-name {
    color: var(--band-gold);
    font-weight: 600;
    letter-spacing: 0;
    text-transform: uppercase;
  }
</style>
</head>
<body>
  <main class="cover">
    <svg class="cover-art" width="1200" height="1200" viewBox="0 0 1200 1200" role="img" aria-label="Glitch-art artwork: a symmetrical crystalline shape in cyan, violet and maroon, melting into vertical streaks of colour across the whole cover">
      <defs>
        <linearGradient id="streak-field" x1="0" y1="0" x2="1" y2="0">
          <stop offset="0" stop-color="#1f3a44"/>
          <stop offset="0.18" stop-color="#2f8e9e"/>
          <stop offset="0.5" stop-color="#4cc6d3"/>
          <stop offset="0.82" stop-color="#2f8e9e"/>
          <stop offset="1" stop-color="#2a2430"/>
        </linearGradient>
        <linearGradient id="streak-fade" x1="0" y1="0" x2="0" y2="1">
          <stop offset="0" stop-color="#5a1a24" stop-opacity="0.55"/>
          <stop offset="0.3" stop-color="#5a1a24" stop-opacity="0"/>
          <stop offset="0.8" stop-color="#3a1a22" stop-opacity="0.2"/>
          <stop offset="1" stop-color="#2a1418" stop-opacity="0.85"/>
        </linearGradient>
        <radialGradient id="crystal-mass" cx="0.5" cy="0.55" r="0.5">
          <stop offset="0" stop-color="#4a3f8f"/>
          <stop offset="0.45" stop-color="#5a5cb0"/>
          <stop offset="0.75" stop-color="#56a9c4" stop-opacity="0.85"/>
          <stop offset="1" stop-color="#56a9c4" stop-opacity="0"/>
        </radialGradient>
      </defs>
      <rect class="art-field" x="0" y="0" width="1200" height="1200" fill="url(#streak-field)"/>
      <rect class="art-fade" x="0" y="0" width="1200" height="1200" fill="url(#streak-fade)"/>
      <ellipse class="art-centre" cx="600" cy="720" rx="500" ry="400" fill="url(#crystal-mass)"/>
    </svg>

    <header class="title-row">
      <h1 class="album-title" style="margin:0;font-size:inherit;font-weight:400;">Mirvane</h1>
      <span class="title-divider" aria-hidden="true"></span>
      <p class="band-name" style="margin:0;">kettlesINorbit</p>
    </header>
  </main>
</body>
</html>
```